High-End Print/Digital Ad for Unique Luxury Travel Company Required

Objective:
Design a compelling and visually striking advertisement that highlights our company’s unmatched luxury travel experiences. The ad should elevate our brand image, spark curiosity, and drive prospective clients to contact us.
Target Audience:
• Affluent individuals seeking extraordinary, tailor-made travel experiences
• Affluent, luxury, high-net-worth individuals looking for value, expertise, and white-glove service
• Professionals or retirees who appreciate unique, thoughtfully curated travel over mainstream tourism
Key Messages to Communicate:
• One-of-a-kind luxury travel: Once-in-a-lifetime experiences that are curated with creativity and meticulous attention to detail
• Exceptional service: White-glove, personalized planning from start to finish
• 38 years’ travel experience – expert knowledge of destinations, modes of travel, premium accommodations and well-established, meaningful industry connections.
• Highly trusted: Cruise line executives often say, “No one does what you do.”
Tone and Style:
• Elegant, luxurious, sophisticated
• Eye-catching, polished, and modern
• Professional but warm—conveys trust and credibility
• High-impact visuals (full-bleed imagery, custom graphics, or high-end photography)
Deliverables:
• One full-page print ad and digital ad
• Ready-to-print, high-resolution file + working file (PSD, AI, etc.)
Optional: Social media-optimized version or short motion-graphic variation (if designer offers it)
Inspiration & Visual Style Suggestions:
• Think Velvet Voyager, Brimley Hart Wanderer, Seven Lanterns, or Oriel Retreats ad styles
• Large, emotive imagery with elegant typography
• Clean layout that speaks luxury, clarity, and trust
Copy Direction (draft):
For those who’ve explored the world—and crave something beyond the ordinary.
Each journey is a masterfully curated experience, rich in detail, seamless in execution, and unforgettable in every way.
Founded in 1997, Tidewell Journeys is a unique travel company specializing in cruising, all-inclusive luxury properties, and tours world-wide for individuals, groups, and incentives.
We offer an exceptional range of services designed to ensure every journey is flawlessly executed and truly unforgettable.
Let us help you plan your next extraordinary adventure.
Note: You may refine the copy slightly based on layout or format needs.
Other Resources for References:
1. Website - www.tidewelljourneys.example

```html
<!DOCTYPE html>
<html lang="en">
<head>
<meta charset="utf-8">
<title>Tidewell Journeys – A Luxury Travel Company</title>
<link rel="stylesheet" href="https://fonts.googleapis.com/css2?family=Bodoni+Moda:opsz,wght@6..96,500;6..96,600&family=Josefin+Sans:wght@300&family=Montserrat:wght@700&family=Questrial&display=swap">
<style>
  :root {
    --page-bg: #ffffff;
    --sky-deep: #0050a8;
    --sky-mid: #0a84c6;
    --sky-light: #3aa3dc;
    --haze: #8cc4e6;
    --lagoon: #2ec4c6;
    --shore: #bfe8e6;
    --sand: #e9ebec;
    --sand-shadow: #cdd2d8;
    --ink-light: #fbf9f6;
    --ink-dark: #2f3337;
  }
  html, body {
    margin: 0;
    width: 1200px;
    height: 1200px;
    overflow: hidden;
    background: var(--page-bg);
  }
  .ad {
    position: absolute;
    left: 175px;
    top: 50px;
    width: 851px;
    height: 1100px;
  }
  .ad svg { display: block; }
  .brand-title {
    font-family: "Bodoni Moda", "Didot", serif;
    font-weight: 500;
    fill: var(--ink-light);
  }
  .brand-subtitle {
    font-family: "Josefin Sans", sans-serif;
    font-weight: 300;
    fill: var(--ink-light);
  }
  .tagline {
    font-family: "Montserrat", sans-serif;
    font-weight: 700;
    fill: var(--ink-light);
  }
  .founded {
    font-family: "Bodoni Moda", serif;
    font-weight: 600;
    fill: var(--ink-light);
  }
  .founded-rule { stroke: var(--ink-light); stroke-width: 1.4; }
  .about {
    font-family: "Questrial", sans-serif;
    fill: var(--ink-dark);
  }
</style>
</head>
<body>
  <div class="ad">
    <svg width="851" height="1100" viewBox="0 0 851 1100" xmlns="http://www.w3.org/2000/svg">
      <defs>
        <linearGradient id="beach-tones" x1="0" y1="0" x2="0" y2="1">
          <stop offset="0" stop-color="var(--sky-deep)"/>
          <stop offset="0.35" stop-color="var(--sky-mid)"/>
          <stop offset="0.5" stop-color="var(--sky-light)"/>
          <stop offset="0.6" stop-color="var(--haze)"/>
          <stop offset="0.67" stop-color="var(--sky-mid)"/>
          <stop offset="0.685" stop-color="var(--lagoon)"/>
          <stop offset="0.74" stop-color="var(--shore)"/>
          <stop offset="0.8" stop-color="var(--sand)"/>
          <stop offset="1" stop-color="var(--sand-shadow)"/>
        </linearGradient>
      </defs>

      <rect class="hero-photo" width="851" height="1100" fill="url(#beach-tones)"
            role="img" aria-label="Photo: a woman in a red polka-dot sundress walking barefoot along a white sandbar between turquoise shallows under a bright blue sky"/>

      <text class="brand-title" x="40" y="224" font-size="190" textLength="756" lengthAdjust="spacingAndGlyphs">TIDEWELL</text>
      <text class="brand-title" x="47" y="375" font-size="190" textLength="757" lengthAdjust="spacingAndGlyphs">JOURNEYS</text>

      <text class="brand-subtitle" x="82" y="434" font-size="44" textLength="694" lengthAdjust="spacingAndGlyphs">A LUXURY TRAVEL COMPANY</text>

      <g class="tagline" font-size="56">
        <text x="82" y="579" textLength="218" lengthAdjust="spacingAndGlyphs">NO ONE</text>
        <text x="82" y="645" textLength="157" lengthAdjust="spacingAndGlyphs">DOES</text>
        <text x="84" y="710" textLength="172" lengthAdjust="spacingAndGlyphs">WHAT</text>
        <text x="84" y="776" textLength="225" lengthAdjust="spacingAndGlyphs">YOU DO</text>
      </g>

      <g class="founded-mark">
        <text class="founded" x="672" y="559" font-size="37" text-anchor="middle" textLength="182" lengthAdjust="spacingAndGlyphs">FOUNDED</text>
        <line class="founded-rule" x1="594" y1="577" x2="643" y2="577"/>
        <text class="founded" x="672" y="590" font-size="37" text-anchor="middle">IN</text>
        <line class="founded-rule" x1="701" y1="577" x2="750" y2="577"/>
        <text class="founded" x="672" y="625" font-size="37" text-anchor="middle">1997</text>
      </g>

      <g class="about" font-size="19" text-anchor="middle">
        <text x="424" y="1010" textLength="740" lengthAdjust="spacingAndGlyphs">TIDEWELL JOURNEYS IS A UNIQUE TRAVEL COMPANY SPECIALIZING IN CRUISING,</text>
        <text x="424" y="1033" textLength="712" lengthAdjust="spacingAndGlyphs">ALL-INCLUSIVE LUXURY PROPERTIES, AND TOURS WORLD-WIDE FOR</text>
        <text x="424" y="1056" textLength="392" lengthAdjust="spacingAndGlyphs">INDIVIDUALS, GROUPS, AND INCENTIVES.</text>
      </g>
    </svg>
  </div>
</body>
</html>
```